Venture Capital Firm Needs Website Redesign

We need a bold revamp of our website (https://halvenmoor.vc/)
which at the moment looks washed out. We want a crisp, fresh and unique look. Feel free to keep as much or as little content in the site. The only thing we need to keep is a team section. The site should convey a clear distinction between our 3 product lines: Venture Capital, Private Credit, and Crypto. Two versions of our logo are attached and they should not change. For design inspirations, we like http://www.plumridgecap.com/ for a more simple site and for a more built out site we like http://tallowgate.com/

Updates
Industry/Entity Type
Investment
Coding
Coded - Design and coding required
Number of Pages Required
1 page
Font styles to use
Colors
Designer to choose colors to be used in the design.
Requirements
Must have
- - Clear distinction between our 3 product lines: Venture Capital, Private Credit
- - Team section

Nice to have
- Some really creative aspect like http://www.plumridgecap.com/ has with the distinction between first, second, and third kind

```html
<!DOCTYPE html>
<html lang="en">
<head>
<meta charset="utf-8">
<title>Halvenmoor</title>
<link href="https://fonts.googleapis.com/css2?family=Open+Sans:wght@300;400;600;700&display=swap" rel="stylesheet">
<style>
:root{
  --green:#8cb33a;
  --green-dark:#6f9427;
  --ink:#2b2e31;
  --body:#5a5e62;
  --night:#1c2024;
  --slate:#3b3f43;
  --paper:#ffffff;
  --mist:#f2f3f4;
  --line:#d9dcdf;
}
*{box-sizing:border-box;margin:0;padding:0}
html,body{width:1200px;height:5000px;overflow:hidden}
body{position:relative;background:var(--paper);font-family:"Open Sans",Arial,sans-serif;color:var(--body)}
.abs{position:absolute}

/* hero */
.topbar{position:absolute;left:0;top:0;width:1200px;height:933px;background:linear-gradient(180deg,#24303a 0%,#1b2730 55%,#14181c 100%)}
.hero-photo{position:absolute;left:0;top:0;width:1200px;height:640px;background:radial-gradient(ellipse at 70% 30%,#4d6f8a 0%,#2a4356 40%,#1b2a35 75%,#161d23 100%)}
.contact-pill{position:absolute;right:40px;top:0;height:42px;padding:0 26px;background:var(--green);border-radius:0 0 0 22px;display:flex;align-items:center;gap:22px;color:#fff;font-size:14px}
.contact-pill span{display:flex;align-items:center;gap:7px}
.dot{width:12px;height:12px;border-radius:50%;background:#fff;display:inline-block}
.brand{position:absolute;left:46px;top:80px;font-size:38px;font-weight:400;color:#fff;letter-spacing:1px}
.nav{position:absolute;right:40px;top:90px;display:flex;gap:28px;font-size:13px;font-weight:400;color:#fff;text-transform:uppercase}
.nav a{color:#fff;text-decoration:none;padding-bottom:8px}
.nav a.active{color:var(--green);border-bottom:3px solid var(--green)}
.hero-title{position:absolute;left:0;width:1200px;top:385px;text-align:center;font-size:42px;line-height:54px;color:#fff;font-weight:300}
.hero-title b{color:var(--green);font-weight:300}
.btn-green{display:inline-block;background:var(--green);color:#fff;font-size:18px;padding:10px 48px;border-radius:3px}
.hero-cta{position:absolute;top:508px;left:0;width:1200px;text-align:center}
.hero-intro{position:absolute;left:150px;width:900px;top:660px;text-align:center;color:#e6e8ea;font-size:15px;line-height:24px}
.btn-outline{position:absolute;left:500px;top:782px;width:200px;height:40px;border:2px solid #fff;border-radius:4px;color:#fff;font-size:15px;line-height:36px;text-align:center}
.hero-slant{position:absolute;left:0;top:880px;width:1200px;height:60px;background:var(--paper);clip-path:polygon(0 100%,100% 0,100% 100%)}

/* section titles */
.sec-title{display:flex;align-items:center;font-size:26px;font-weight:400;color:var(--ink);text-transform:uppercase;letter-spacing:1px}
.sec-title.light{color:#fff}
.sec-title .accent{color:var(--green)}

/* photo circles */
.photo-circle{position:absolute;border-radius:50%;border:10px solid #fff;box-shadow:0 8px 20px rgba(0,0,0,.25)}

/* venture capital */
.vc-photo{left:67px;top:1033px;width:300px;height:300px;background:linear-gradient(160deg,#d7dde2 0%,#8795a1 45%,#2a323a 100%)}
.vc-title{left:466px;top:1022px}
.vc-copy{left:466px;top:1110px;width:660px;font-size:15px;line-height:24px}
.badge-row{position:absolute;display:flex;gap:12px}
.badge{width:154px;height:74px;border:1px solid var(--line);border-radius:4px;background:#fff;display:flex;align-items:center;justify-content:center}
.badge i{width:70px;height:24px;border-radius:4px;background:#c7ccd1}
.vc-badges{left:466px;top:1238px}

/* private credit */
.credit{position:absolute;left:0;top:1450px;width:1200px;height:600px;background:linear-gradient(180deg,#3f4448 0%,#2e3236 100%);clip-path:polygon(0 10%,100% 0,100% 90%,0 100%)}
.credit-title{left:0;width:1200px;top:1604px;justify-content:center}
.credit-copy{left:150px;width:900px;top:1680px;color:#e0e3e5;font-size:15px;line-height:24px;text-align:center}
.credit-badges{left:357px;top:1808px}
.credit-badges .badge{background:transparent;border-color:#8a9095}
.credit-badges .badge i{background:#7f868c}

/* crypto */
.crypto-title{left:67px;top:2144px}
.crypto-copy{left:67px;top:2225px;width:680px;font-size:15px;line-height:24px}
.crypto-copy p{margin-bottom:18px}
.crypto-photo{left:783px;top:2133px;width:300px;height:300px;background:radial-gradient(circle at 50% 45%,#d6f07a 0%,#7fbf2a 35%,#2f6a12 75%,#12240a 100%)}

/* team */
.team{position:absolute;left:0;top:2567px;width:1200px;height:783px;background:linear-gradient(180deg,#3a3e42 0%,#2a2e32 100%);clip-path:polygon(0 0,100% 8%,100% 100%,0 92%)}
.team-title{left:0;width:1200px;top:2714px;justify-content:center}
.team-sub{left:0;width:1200px;top:2810px;text-align:center;color:#fff;font-size:18px}
.member{position:absolute;top:2883px;width:240px;text-align:center;color:#fff}
.member .face{width:217px;height:217px;margin:0 auto;border-radius:50%;border:8px solid #fff;background:linear-gradient(180deg,#c9ccce 0%,#8b9094 100%)}
.member.featured .face{border-color:var(--green)}
.member h3{margin-top:20px;font-size:18px;font-weight:600}
.member p{font-size:15px;color:#d0d4d7}
.socials{display:flex;justify-content:center;gap:12px;margin-top:12px}
.socials i{width:16px;height:16px;border-radius:3px;background:#c5c9cc}
.arrow{position:absolute;top:2968px;color:#fff;font-size:32px}

/* blog */
.blog-title{left:0;width:1200px;top:3444px;justify-content:center}
.post{position:absolute;top:3533px;width:264px;background:var(--mist);text-align:center;padding-bottom:26px}
.post .thumb{height:166px;background:linear-gradient(160deg,#dfe7ee 0%,#9fb2c2 55%,#5d6e7c 100%)}
.post h3{color:var(--green);font-size:17px;font-weight:600;margin:16px 0 10px}
.post p{font-size:12px;line-height:18px;padding:0 16px;text-align:left}
.post .btn-dark{display:inline-block;margin-top:14px;background:var(--night);color:#fff;font-size:12px;padding:6px 26px}

/* contact */
.contact{position:absolute;left:0;top:3950px;width:1200px;height:717px;background:linear-gradient(180deg,#1d2a1a 0%,#26321f 50%,#1a2016 100%);clip-path:polygon(0 0,100% 10%,100% 100%,0 95%)}
.contact-title{left:0;width:1200px;top:4119px;justify-content:center}
.contact-sub{left:0;width:1200px;top:4210px;text-align:center;color:#fff;font-size:18px}
.field{position:absolute;height:48px;background:rgba(255,255,255,.18);color:#fff;font-size:15px;padding:13px 14px}
.submit{position:absolute;left:500px;top:4482px;width:200px;height:38px;background:var(--green);color:#fff;font-size:14px;font-weight:600;text-align:center;line-height:38px}

/* footer */
.footer-brand{left:50px;top:4770px;width:230px;text-align:center;font-size:26px;font-weight:400;color:var(--ink)}
.f-col{position:absolute;top:4720px;font-size:13px;line-height:20px;color:var(--body)}
.f-col h4{font-size:14px;color:var(--ink);text-transform:uppercase;margin-bottom:10px;font-weight:700}
.f-row{display:flex;align-items:center;gap:8px;margin-bottom:8px}
.f-row .ic{width:20px;height:20px;border-radius:50%;border:1px solid #888;flex:none}
.f-row .sq{width:18px;height:18px;border-radius:3px;background:#4a6a9a;flex:none}
.signup{display:flex;margin-top:6px}
.signup span{width:170px;height:38px;border:1px solid var(--ink);font-size:12px;padding:10px}
.signup b{height:38px;background:var(--night);color:#fff;font-size:12px;padding:11px 14px}
.copyright{position:absolute;left:0;top:4967px;width:1200px;height:33px;background:var(--green);color:#fff;text-align:center;font-size:12px;line-height:33px;font-weight:600}
</style>
</head>
<body>

<header class="topbar">
  <div class="hero-photo" role="img" aria-label="Hand touching a glowing growth chart on a dark blue screen"></div>
  <div class="contact-pill"><span><i class="dot"></i>1-888-555-0148</span><span><i class="dot"></i>info@halvenmoor.vc</span><span><i class="dot"></i><i class="dot"></i><i class="dot"></i></span></div>
  <div class="brand">Halvenmoor</div>
  <nav class="nav"><a class="active">About</a><a>Venture Capital</a><a>Private Credit</a><a>Crypto</a><a>Team</a><a>Blog</a><a>Contact</a></nav>
  <h1 class="hero-title"><b>Halvenmoor</b> operates at the intersection of technology<br>and novel asset classes.</h1>
  <div class="hero-cta"><span class="btn-green">Get Started</span></div>
  <p class="hero-intro">Halvenmoor operates three businesses that bridge technology and finance. We invest in pre-seed venture capital, and build software for the companies we invest in. We manage direct private credit funds that provide capital to alternative credit platforms, enabling them to finance the loans they originate. We create crypto funds for individuals, IRAs and institutions to get simple and easy access to cryptocurrencies.</p>
  <div class="btn-outline">Learn More</div>
  <div class="hero-slant"></div>
</header>

<section>
  <div class="photo-circle vc-photo" role="img" aria-label="Businessman holding a tablet with a rising chart"></div>
  <h2 class="abs sec-title vc-title">Venture&nbsp;<span class="accent">Capital</span></h2>
  <p class="abs vc-copy">Halvenmoor invests in early-stage startups led by founders who are passionate and knowledgeable about the markets they serve. We have our own software developers and product managers. We work with the founders in our portfolio to help them bring products to market, earning equity for this work and for the cash we invest in their companies.</p>
  <div class="badge-row vc-badges"><div class="badge"><i></i></div><div class="badge"><i></i></div><div class="badge"><i></i></div><div class="badge"><i></i></div></div>
</section>

<section class="credit" role="img" aria-label="Dark toned photo of hands working over financial papers"></section>
<h2 class="abs sec-title light credit-title">Private Credit</h2>
<p class="abs credit-copy">Halvenmoor Private Credit provides capital to lending businesses that are focused on using technology to establish new credit markets, create new credit products or dramatically re-invent an existing form of credit. We believe that the pioneers who build something truly different in a credit market will create the most sustainable business models. Given our heritage as a venture firm, we are comfortable with emerging businesses and can provide capital for a company's first loan.</p>
<div class="badge-row credit-badges"><div class="badge"><i></i></div><div class="badge"><i></i></div><div class="badge"><i></i></div></div>

<section>
  <h2 class="abs sec-title crypto-title">Crypto</h2>
  <div class="abs crypto-copy">
    <p>Halvenmoor Crypto is a multi-strategy cryptocurrency asset management firm.</p>
    <p>The Halvenmoor Crypto Index tracks the top 15 cryptocurrencies weighted by market cap and rebalanced twice a month. We believe this is the simplest and most cost-effective way to obtain cryptocurrency exposure. Our process has been designed by experts from financial services and cryptocurrency industries.</p>
  </div>
  <div class="photo-circle crypto-photo" role="img" aria-label="Glowing green network globe"></div>
</section>

<section class="team" role="img" aria-label="Dark city crowd photo behind the team"></section>
<h2 class="abs sec-title light team-title">Our&nbsp;<span class="accent">Team</span></h2>
<p class="abs team-sub">The very best helping the very best.</p>
<div class="arrow" style="left:70px">&#8249;</div>
<div class="arrow" style="left:1112px">&#8250;</div>
<div class="member featured" style="left:130px"><div class="face" role="img" aria-label="Portrait of Corin Vale"></div><h3>Corin Vale</h3><p>Partner</p><div class="socials"><i></i><i></i><i></i><i></i></div></div>
<div class="member" style="left:363px"><div class="face" role="img" aria-label="Portrait of Tobin Aldercott"></div><h3>Tobin Aldercott</h3><p>Partner</p><div class="socials"><i></i><i></i><i></i><i></i></div></div>
<div class="member" style="left:597px"><div class="face" role="img" aria-label="Portrait of Ravi Sennet"></div><h3>Ravi Sennet</h3><p>Partner</p><div class="socials"><i></i><i></i><i></i><i></i></div></div>
<div class="member" style="left:830px"><div class="face" role="img" aria-label="Portrait of Marcus Lindqvist"></div><h3>Marcus Lindqvist</h3><p>Partner</p><div class="socials"><i></i><i></i><i></i><i></i></div></div>

<section>
  <h2 class="abs sec-title blog-title">From&nbsp;<span class="accent">Our Blog</span></h2>
  <article class="post" style="left:157px"><div class="thumb" role="img" aria-label="Hands reviewing charts on a tablet"></div><h3>Blog Post #1</h3><p>Lorem ipsum dolor sit amet, consectetuer adipiscing elit, sed diam nonummy nibh euismod tincidunt ut laoreet dolore magna aliquam.</p><span class="btn-dark">Read More</span></article>
  <article class="post" style="left:468px"><div class="thumb" role="img" aria-label="Business team meeting around a table"></div><h3>Blog Post #2</h3><p>Lorem ipsum dolor sit amet, consectetuer adipiscing elit, sed diam nonummy nibh euismod tincidunt ut laoreet dolore magna aliquam.</p><span class="btn-dark">Read More</span></article>
  <article class="post" style="left:779px"><div class="thumb" role="img" aria-label="Hand pointing at printed financial charts"></div><h3>Blog Post #3</h3><p>Lorem ipsum dolor sit amet, consectetuer adipiscing elit, sed diam nonummy nibh euismod tincidunt ut laoreet dolore magna aliquam.</p><span class="btn-dark">Read More</span></article>
</section>

<section class="contact" role="img" aria-label="Dark green photo of office glass panels"></section>
<h2 class="abs sec-title light contact-title">Contact&nbsp;<span class="accent">Us</span></h2>
<p class="abs contact-sub">We would love to hear from you.</p>
<div class="field" style="left:117px;top:4270px;width:310px">Your Name</div>
<div class="field" style="left:445px;top:4270px;width:310px">Your Email</div>
<div class="field" style="left:773px;top:4270px;width:310px">Your Subject</div>
<div class="field" style="left:117px;top:4332px;width:966px;height:135px">Message</div>
<div class="submit">SUBMIT</div>

<footer>
  <div class="abs footer-brand">Halvenmoor</div>
  <div class="f-col" style="left:310px"><h4>Quick Links</h4>Venture Capital<br>Private Credit<br>Crypto<br>About<br>Team<br>Blog<br>Contact</div>
  <div class="f-col" style="left:475px"><h4>Contact</h4>
    <div class="f-row"><i class="ic"></i><span>Halvenmoor<br>218 Marlow Street, Suite 410<br>New York, NY 10013</span></div>
    <div class="f-row"><i class="ic"></i><span>1-888-555-0148</span></div>
    <div class="f-row"><i class="ic"></i><span>info@halvenmoor.vc</span></div>
  </div>
  <div class="f-col" style="left:718px"><h4>Follow Us</h4>
    <div class="f-row"><i class="sq"></i><span>Newsroom</span></div>
    <div class="f-row"><i class="sq"></i><span>Updates</span></div>
    <div class="f-row"><i class="sq"></i><span>Network</span></div>
  </div>
  <div class="f-col" style="left:875px"><h4>Newsletter</h4><div class="signup"><span>Enter Email Address</span><b>SIGN UP</b></div></div>
  <div class="copyright">COPYRIGHT © 2018 HALVENMOOR. ALL RIGHTS RESERVED.</div>
</footer>

</body>
</html>
```